Pet Shop Website

website will need to have the following features:
• Photo Galleries of each species (Dogs, Cats, Birds, Fish, Reptiles, Rabbits) in a light box popup
o Each species may have several different categories for example:
 Fish
• Marine fish
• Fresh water
• tropical
• Cichlid
• Information Fact sheets of each species – Downloaded as a pdf which can be either
o Care Sheets
o Training Sheets
• Members Area
o Username (Email Address) & Password login
o New signups
o Exclusive Member Deals
o Newsletter options

The front page must be very simple (for example lumavale.com.au) contain the following:
• Product of the week - which can be purchased online
o Short details
o Cost
• Pet Club Sign up picture
• Animal of the week/month
• Contact Phone Number and addresses of the stores
• A jQuery slideshow (Images could include stores, pets etc…)
The main page MUST keep simple. We do not want it cluttered.

Inner Page
The animals / reptile page will need to have:
• Short description of the species
• Photo Galleries
• A list of what is in stock and the list needs to clearly be sorted by each store (Use of Tabs maybe).
• Facts sheets / Info sheets
The type of website ideas (not the type of look that we are necessary after) is and the sort of content that we want to offer are as follows:

http://www.scalenook.com.au/
http://www.marrowdenpets.com.au/
http://www.thefurloft.com.au
http://www.critterhaven.net.au

Colour in the new website:
Blue
Red
Grey
Yellow

Original site:

http://www.pawglint.com.au
Updates

Hi Guys,

We had feedback from the client and they would like to see a few dark designs.

Thanks                                   

Reason: We would like to reopen this contest back up for a further week

Target Market(s)

Targeting animal lovers

Industry/Entity Type

Store

Requirements
Should not have
• Alter the logo in anyway

```html
<!DOCTYPE html>
<html lang="en">
<head>
<meta charset="utf-8">
<title>Pawglint – Pet Shop</title>
<link rel="stylesheet" href="https://fonts.googleapis.com/css2?family=Open+Sans:wght@400;600;700&family=Oswald:wght@400;500&family=Arimo:wght@400;700&display=swap">
<style>
:root{
  --bar:#1e1e1e; --footer:#262626; --footer-base:#1a1a1a;
  --paper:#e8e8e8; --white:#fff; --ink:#333; --muted:#777;
  --red:#d71f1f; --red-dark:#b30f0f; --navy:#14246b; --blue-link:#0b2a8c;
  --yellow:#f7c400; --yellow-dark:#e3a700; --sky:#e4f1fb; --line:#ddd;
  --buy:#2e9be6; --gold:#a88c4e;
}
*{box-sizing:border-box;margin:0;padding:0}
html,body{width:1136px;height:1200px;overflow:hidden;background:var(--paper)}
body{font-family:Arimo,Arial,sans-serif;color:var(--ink)}
.stage{position:absolute;left:0;top:0;width:1420px;height:1500px;transform:scale(.8);transform-origin:0 0;background:var(--paper)}
.abs{position:absolute;white-space:nowrap}
.topbar{left:0;top:0;width:1420px;height:50px;background:var(--bar);color:#eee;font-size:12px}
.topbar span{position:absolute;top:17px}
.cart-icon{left:488px;top:15px;width:22px;height:16px;background:var(--yellow);border-radius:2px}
.flag{left:1010px;top:17px;width:22px;height:14px;background:#2b3f8f;border:2px solid #fff;outline:1px solid var(--red)}
.currency{left:1119px;top:14px;width:68px;height:21px;background:#111;border:1px solid #333;color:#888;font-size:12px;padding:3px 5px}
.currency:after{content:"";position:absolute;right:6px;top:8px;border:4px solid transparent;border-top-color:#888}
.brand{left:190px;top:88px;display:flex;align-items:center;gap:12px;font-family:'Open Sans',sans-serif;font-weight:700;font-size:40px;color:var(--navy)}
.brand i{width:30px;height:30px;background:var(--yellow)}
.store-addr{right:242px;top:72px;text-align:right;font-size:16px;line-height:25px;color:#222}
.store-phone{right:242px;top:132px;font-size:32px;color:var(--navy)}
.strip{left:188px;top:185px;width:1000px;height:11px;background:var(--white)}
.nav{left:188px;top:196px;width:1000px;height:64px;background:linear-gradient(#e42323,#c10f0f)}
.nav a{position:absolute;top:22px;color:#fff;font:600 15px 'Open Sans',sans-serif;text-decoration:none}
.nav .sep{position:absolute;top:12px;width:1px;height:40px;background:#a60c0c}
.search{left:740px;top:12px;width:245px;height:40px;background:#fff;border:1px solid #ccc;color:#999;font-size:12px;padding:13px 10px}
.search b{position:absolute;right:6px;top:6px;width:26px;height:26px;background:var(--red)}
.panel{left:188px;top:260px;width:1000px;height:958px;background:var(--white)}
.hero{left:188px;top:260px;width:719px;height:452px;background:linear-gradient(110deg,#fff 0%,#f3ece6 40%,#d9c6b2 70%,#e9e9ee 100%)}
.hero-title{left:488px;top:320px;font:500 46px/48px Oswald,sans-serif;color:var(--red)}
.hero-sub{left:488px;top:366px;font:400 29px/32px Oswald,sans-serif;color:#333}
.hero-cta{left:189px;top:603px;width:200px;height:43px;background:var(--red);color:#fff;font:400 19px/43px Oswald,sans-serif;padding:0 11px}
.dots{left:826px;top:687px;display:flex;gap:2px}
.dots i{width:15px;height:15px;border-radius:50%;background:#888}
.dots i:first-child{background:var(--yellow)}
.side-h{font:600 15px 'Open Sans',sans-serif;color:#333}
.field{width:245px;height:43px;background:#fff;border:1px solid #ddd;color:#999;font-size:12px;padding:14px 12px}
.btn-y{width:87px;height:44px;background:linear-gradient(#ffd93a,var(--yellow-dark));border:1px solid #d49b00;color:#8a4b00;font:700 12px Arimo,sans-serif;text-align:center;padding-top:15px}
.divider{height:1px;background:var(--line)}
.newsbox{left:908px;top:532px;width:280px;height:180px;background:linear-gradient(90deg,var(--sky),#f5fafe)}
.vline{width:1px;background:var(--line)}
.thumb{width:150px;height:131px;border:1px solid var(--line);padding:3px}
.thumb div{width:100%;height:100%}
.arrows{left:499px;top:731px;width:32px;height:21px;border-radius:11px;background:#666}
.btn-dark{background:#1b1b1b;color:#fff;font-size:13px;padding:9px 7px}
.prod-img{width:157px;height:139px;border:1px solid var(--line);padding:6px}
.prod-img div{width:100%;height:100%}
.prod-txt{font-size:12px;line-height:17px;color:#222;width:170px;white-space:normal}
.price{font-size:18px;color:var(--red)}
.buy{width:67px;height:30px;background:linear-gradient(#68c3ff,var(--buy));border:1px solid #1c7fc4;color:#0d4f85;font:700 14px Arimo,sans-serif;text-align:center;padding-top:6px}
.download{left:909px;top:1116px;width:240px;height:58px;background:linear-gradient(#f32626,#c80b0b);border:1px solid #a00;color:#fff;font:400 24px 'Open Sans',sans-serif;text-align:center;padding-top:11px}
.footer{left:0;top:1238px;width:1420px;height:220px;background:var(--footer)}
.footer-base{left:0;top:1458px;width:1420px;height:42px;background:var(--footer-base);color:#777;font-size:12px}
.fcol h4{font:600 15px 'Open Sans',sans-serif;color:#ccc;margin-bottom:18px}
.fcol li{list-style:none;font-size:12px;color:#888;margin-bottom:14px}
.social li{display:flex;align-items:center;gap:6px;margin-bottom:17px}
.social i{width:22px;height:22px;background:#555}
.stores h5{font:600 12px 'Open Sans',sans-serif;color:#bbb;margin-bottom:8px}
.stores p{font-size:12px;line-height:22px;color:#777}
</style>
</head>
<body>
<div class="stage">
  <div class="abs topbar">
    <span style="left:199px">Welcome, ( Log in )</span>
    <i class="abs cart-icon"></i>
    <span style="left:523px">Shopping cart: Now in your cart 0 items</span>
    <span style="left:907px">Home &nbsp;| &nbsp;Log In &nbsp;|</span>
    <i class="abs flag"></i>
    <span style="left:1046px">| &nbsp;Currencies:</span>
    <div class="abs currency">Dollar</div>
  </div>

  <div class="abs brand"><i></i>Pawglint</div>
  <div class="abs store-addr">Shop 4 / 220 Tallow Rd<br>BRIARDALE, W.A 6190</div>
  <div class="abs store-phone">(08) 9000 4170</div>

  <div class="abs strip"></div>
  <nav class="abs nav">
    <a style="left:52px">HOME</a><i class="sep" style="left:134px"></i>
    <a style="left:162px">ABOUT US</a><i class="sep" style="left:271px"></i>
    <a style="left:301px">PETS</a><i class="sep" style="left:375px"></i>
    <a style="left:398px">CONTACT US</a><i class="sep" style="left:520px"></i>
    <div class="abs search">Search<b></b></div>
  </nav>

  <div class="abs panel"></div>

  <section class="abs hero" role="img" aria-label="Photo of three dogs wearing bandanas and a jersey"></section>
  <div class="abs hero-title">LOVE YOUR PET</div>
  <div class="abs hero-sub">SPRING APPAREL IS HERE!</div>
  <div class="abs hero-cta">SHOP THE COLLECTION &#9656;</div>
  <div class="abs dots"><i></i><i></i><i></i><i></i></div>

  <div class="abs vline" style="left:907px;top:260px;height:452px"></div>
  <div class="abs side-h" style="left:927px;top:280px">MEMBER LOGIN</div>
  <div class="abs divider" style="left:920px;top:311px;width:253px"></div>
  <div class="abs field" style="left:926px;top:326px">Email Address</div>
  <div class="abs field" style="left:926px;top:377px">Password</div>
  <div class="abs btn-y" style="left:925px;top:429px">LOGIN</div>
  <div class="abs" style="left:931px;top:490px;font-size:12px;color:var(--blue-link)">Forgot Password?</div>
  <div class="abs" style="left:931px;top:512px;font-size:12px;color:#444">New User <span style="color:var(--blue-link)">Sign Up</span> Here</div>

  <div class="abs newsbox"></div>
  <div class="abs side-h" style="left:927px;top:553px">NEWLETTER</div>
  <div class="abs divider" style="left:920px;top:584px;width:253px"></div>
  <div class="abs" style="left:931px;top:599px;font-size:12px">Signup for free news letter</div>
  <div class="abs field" style="left:926px;top:622px;height:33px;padding-top:10px">Email Address</div>
  <div class="abs btn-y" style="left:925px;top:663px;height:35px;padding-top:11px">SUBMIT</div>

  <div class="abs divider" style="left:188px;top:712px;width:1000px"></div>
  <div class="abs side-h" style="left:212px;top:733px">PHOTO GALLERY</div>
  <svg class="abs arrows" viewBox="0 0 32 21" aria-label="Previous and next">
    <path d="M12 7l-4 3.5 4 3.5M20 7l4 3.5-4 3.5" fill="none" stroke="#fff" stroke-width="1.6"/>
  </svg>
  <div class="abs divider" style="left:202px;top:764px;width:333px"></div>
  <div class="abs thumb" style="left:215px;top:781px"><div role="img" aria-label="Photo of a Saint Bernard puppy" style="background:linear-gradient(135deg,#f3eee9,#a8643a 55%,#f1ece6)"></div></div>
  <div class="abs thumb" style="left:380px;top:781px"><div role="img" aria-label="Photo of a tabby kitten" style="background:linear-gradient(135deg,#fff,#9a8a78 55%,#fff)"></div></div>
  <div class="abs vline" style="left:547px;top:712px;height:218px"></div>

  <div class="abs" role="img" aria-label="Photo of a poodle in a pink polka-dot dress" style="left:548px;top:745px;width:140px;height:165px;background:linear-gradient(#fff,#f0c8d6 60%,#fff)"></div>
  <div class="abs" style="left:694px;top:786px;font:700 34px/40px 'Open Sans',sans-serif;color:var(--red)">ANIMAL</div>
  <div class="abs" style="left:694px;top:829px;font:600 15px/20px 'Open Sans',sans-serif;color:#555">OF THE WEEK/MONTH</div>
  <div class="abs btn-dark" style="left:697px;top:862px">CLICK HERE</div>
  <div class="abs vline" style="left:876px;top:712px;height:506px"></div>

  <div class="abs" style="left:900px;top:740px;font:600 46px/42px 'Open Sans',sans-serif;color:#222">CAT</div>
  <div class="abs" style="left:900px;top:780px;font:700 46px/42px 'Open Sans',sans-serif;color:var(--gold)">DEALS</div>
  <div class="abs" style="left:903px;top:826px;font:600 26px/30px 'Open Sans',sans-serif;color:#aaa">20% OFF</div>
  <div class="abs btn-dark" style="left:905px;top:872px">CLICK HERE</div>
  <div class="abs" role="img" aria-label="Photo of a kitten raising a paw" style="left:1055px;top:745px;width:115px;height:185px;background:linear-gradient(#fff,#a49a90 50%,#d8d2cc)"></div>

  <div class="abs divider" style="left:188px;top:930px;width:1000px"></div>
  <div class="abs side-h" style="left:205px;top:953px">PRODUCT OF THE WEEK</div>
  <div class="abs divider" style="left:195px;top:985px;width:672px"></div>

  <div class="abs prod-img" style="left:206px;top:997px"><div role="img" aria-label="Photo of a carpeted cat scratching post" style="background:linear-gradient(#fff,#d9b58e 50%,#fff)"></div></div>
  <div class="abs prod-txt" style="left:207px;top:1144px">Set conse ctetur adipisicing eli ipsum dolor sit amet</div>
  <div class="abs price" style="left:206px;top:1186px">$75.00</div>
  <div class="abs buy" style="left:294px;top:1181px">BUY</div>

  <div class="abs prod-img" style="left:454px;top:997px"><div role="img" aria-label="Photo of a woven pet carrier bag with a small dog" style="background:linear-gradient(#fff,#d9c28a 50%,#7fc9d6)"></div></div>
  <div class="abs prod-txt" style="left:455px;top:1144px">Adipisicing eli ipsum dolor sit amet</div>
  <div class="abs price" style="left:454px;top:1186px">$37.00</div>
  <div class="abs buy" style="left:542px;top:1181px">BUY</div>

  <div class="abs prod-img" style="left:701px;top:997px"><div role="img" aria-label="Photo of a brown pet supply tote" style="background:linear-gradient(#fff,#5a3322 50%,#7bc3c3)"></div></div>
  <div class="abs prod-txt" style="left:702px;top:1144px">Ctetur adipisicing eli ipsum dolor sit amet</div>
  <div class="abs price" style="left:701px;top:1186px">$45.00</div>
  <div class="abs buy" style="left:789px;top:1181px">BUY</div>

  <div class="abs side-h" style="left:905px;top:953px">FACT SHEETS</div>
  <div class="abs divider" style="left:895px;top:985px;width:273px"></div>
  <div class="abs" style="left:909px;top:1000px;font-size:15px;line-height:25px;color:#333">Downloaded as a pdf<br>which can be either<br>Care Sheets,<br>Training Sheets</div>
  <div class="abs" role="img" aria-label="Illustration of a downloadable document" style="left:1070px;top:1000px;width:98px;height:98px;background:linear-gradient(160deg,#e8e8e8,#f6f6f6 60%,#e2e2e2)"></div>
  <div class="abs download">DOWNLOAD NOW</div>

  <footer class="abs footer"></footer>
  <div class="abs fcol" style="left:207px;top:1262px"><h4>Information</h4><ul><li>Contact</li><li>Sitemap</li><li>Legal Notice</li><li>Terms and conditions</li><li>About us</li></ul></div>
  <div class="abs fcol" style="left:382px;top:1262px"><h4>Our offers</h4><ul><li>New products</li><li>Top sellers</li><li>Specials</li><li>Manufacturers</li><li>Suppliers</li></ul></div>
  <div class="abs fcol" style="left:570px;top:1262px"><h4>Your Account</h4><ul><li>Your Account</li><li>Personal information</li><li>Addresses</li><li>Discount</li><li>Order history</li></ul></div>
  <div class="abs fcol social" style="left:755px;top:1262px"><h4>Follow Us</h4><ul><li><i></i>Chirpline</li><li><i></i>Friendwall</li><li><i></i>Circlepost</li></ul></div>
  <div class="abs stores" style="left:900px;top:1267px">
    <h5>BRIARDALE SUPERSTORE</h5>
    <p>Shop 4 / 220 Tallow Rd BRIARDALE, W.A 6190<br>Phone: (08) 9000 4170, Fax: (08) 9000 4160</p>
    <h5 style="margin-top:17px">FERNWICK LAKE SUPERSTORE</h5>
    <p>Unit 2 / 18 Harbour Drive FERNWICK LAKE, W.A 6171<br>Phone: (08) 9000 6619, Fax: (08) 9000 6613</p>
  </div>
  <div class="abs footer-base">
    <span class="abs" style="left:200px;top:15px">© 2012 Powered by Pawglint. All rights reserved</span>
    <span class="abs" style="left:1153px;top:15px">M3</span>
  </div>
</div>
</body>
</html>
```